Management Services requires simple business card design

Business card design for a management consultancy service that we are establishing. The service will provide project-based services addressing management issues eg investigative, operational and strategic planning, library projects, reporting and customer feedback in government and local government environments. The company name will be Brantwell Management Services (or possibily just Brantwell) and the card should include two names and phones and an email address. We'd like either dark blue or red card with white text if that works??? We want SIMPLE

Industry/Entity Type

Business

```html
<!DOCTYPE html>
<html lang="en">
<head>
<meta charset="utf-8">
<title>Brantwell Management Services – Business Card</title>
<link rel="stylesheet" href="https://fonts.googleapis.com/css2?family=Roboto+Condensed:wght@400&display=swap">
<style>
  :root {
    --backdrop: #2b2b2b;
    --card-navy: #17124a;
    --ink-white: #ffffff;
    --rule: #8d8ab4;
  }
  * { margin: 0; padding: 0; box-sizing: border-box; }
  html, body {
    width: 1200px;
    height: 900px;
    overflow: hidden;
    background: var(--backdrop);
  }
  .card {
    position: absolute;
    left: 276px;
    top: 254px;
    width: 648px;
    height: 392px;
    background: var(--card-navy);
    color: var(--ink-white);
    font-family: "Roboto Condensed", "Arial Narrow", sans-serif;
    font-weight: 400;
  }
  .brand {
    position: absolute;
    left: 58px;
    top: 160px;
    display: inline-block;
  }
  .brand-name {
    display: block;
    font-size: 40px;
    line-height: 1;
    letter-spacing: 1px;
  }
  .brand-tagline {
    display: block;
    margin-top: 6px;
    font-size: 16px;
    line-height: 1;
    letter-spacing: 0.6px;
    text-align: justify;
    text-align-last: justify;
  }
  .contacts {
    position: absolute;
    left: 361px;
    top: 88px;
    width: 240px;
  }
  .contact-name {
    font-size: 25px;
    font-weight: 400;
    letter-spacing: 1.2px;
    line-height: 1;
    margin-bottom: 18px;
  }
  .contact-line {
    display: flex;
    align-items: center;
    gap: 7px;
    font-size: 16px;
    letter-spacing: 0.6px;
    line-height: 23px;
  }
  .contact-line svg {
    width: 13px;
    height: 12px;
    flex: none;
    fill: var(--ink-white);
  }
  .divider {
    width: 226px;
    height: 1px;
    background: var(--rule);
    margin: 18px 0 23px;
  }
</style>
</head>
<body>
  <main class="card">
    <div class="brand">
      <span class="brand-name">Brantwell</span>
      <span class="brand-tagline">Management Services</span>
    </div>

    <section class="contacts">
      <div class="contact">
        <h2 class="contact-name">Allan Brantwell</h2>
        <p class="contact-line">
          <svg viewBox="0 0 13 12" aria-hidden="true"><rect x="0" y="1" width="3" height="11" rx="0.5"/><rect x="4" y="0" width="9" height="12" rx="1"/><rect x="5.5" y="1.5" width="6" height="3" fill="#17124a"/><rect x="5.5" y="6" width="1.5" height="1.5" fill="#17124a"/><rect x="8" y="6" width="1.5" height="1.5" fill="#17124a"/><rect x="5.5" y="8.5" width="1.5" height="1.5" fill="#17124a"/><rect x="8" y="8.5" width="1.5" height="1.5" fill="#17124a"/></svg>
          +61 491 570 156
        </p>
        <p class="contact-line">
          <svg viewBox="0 0 13 12" aria-hidden="true"><path d="M0 2h13v8H0z"/><path d="M0 2l6.5 5L13 2" fill="none" stroke="#17124a" stroke-width="1.2"/></svg>
          ajbrantwell@mailbox.example
        </p>
      </div>

      <div class="divider"></div>

      <div class="contact">
        <h2 class="contact-name">Jo Brantwell</h2>
        <p class="contact-line">
          <svg viewBox="0 0 13 12" aria-hidden="true"><rect x="0" y="1" width="3" height="11" rx="0.5"/><rect x="4" y="0" width="9" height="12" rx="1"/><rect x="5.5" y="1.5" width="6" height="3" fill="#17124a"/><rect x="5.5" y="6" width="1.5" height="1.5" fill="#17124a"/><rect x="8" y="6" width="1.5" height="1.5" fill="#17124a"/><rect x="5.5" y="8.5" width="1.5" height="1.5" fill="#17124a"/><rect x="8" y="8.5" width="1.5" height="1.5" fill="#17124a"/></svg>
          +61 491 570 159
        </p>
        <p class="contact-line">
          <svg viewBox="0 0 13 12" aria-hidden="true"><path d="M0 2h13v8H0z"/><path d="M0 2l6.5 5L13 2" fill="none" stroke="#17124a" stroke-width="1.2"/></svg>
          ajbrantwell@mailbox.example
        </p>
      </div>
    </section>
  </main>
</body>
</html>
```